Business card for Velvet & Lark weddings and events management company
Velvet & Lark
Business card for Velvet & Lark weddings and events management company - Events
Creative Brief
Modern
Nargiza Huseynova
General Manager
17 Samad Str. AZ 1014, Baku, Azerbaijan
nargiza.huseynova@velvetlark-example.az
www.velvetlark-example.az
In addition to english version, be ready to provide azerbaijani version with little changes in titles as seen below: Name: Nərgizə Hüseynova Title: Müdir Address: Samad küç., 17 AZ1014, Bakı, Azərbaycan Slogan on the back: Sevindirməklə sevinirik! (as seen on azerbaijani version of logo, using only capital letters)
HAPPY TO MAKE YOU HAPPY! SEVİNDİRMƏKLƏ SEVİNİRİK! (on azerbaijani version) for this option, you can provide a different font as well, something maybe handwritten and more friendly. (Original font is Trajan Pro)
tulipwanderer tulipwanderer

```html
<!DOCTYPE html>
<html lang="en">
<head>
<meta charset="utf-8">
<title>Velvet &amp; Lark – Business Card</title>
<link href="https://fonts.googleapis.com/css2?family=Roboto:wght@300;400;500&display=swap" rel="stylesheet">
<style>
  :root {
    --backdrop: #2b2b2b;
    --card: #ffffff;
    --ink: #111111;
    --brand-grey: #6e6e6e;
    --muted: #555555;
    --accent-dot: #ffffff;
  }
  * { box-sizing: border-box; margin: 0; padding: 0; }
  html, body {
    width: 1200px; height: 878px; overflow: hidden;
    background: var(--backdrop);
    font-family: "Roboto", Arial, sans-serif;
  }
  .stage { position: relative; width: 1200px; height: 878px; }

  .card {
    position: absolute;
    width: 540px; height: 310px;
    background: var(--card);
    border-radius: 18px;
    box-shadow: 0 10px 30px rgba(0,0,0,.45);
    overflow: hidden;
  }
  .card--back  { left: 130px; top: 110px; }
  .card--front { left: 530px; top: 450px; }

  .brand-name {
    display: flex; align-items: center; gap: 12px;
    font-family: "Roboto", Arial, sans-serif;
    font-weight: 300;
    color: var(--brand-grey);
    white-space: nowrap;
    line-height: 1;
  }
  .brand-name__dot {
    flex: none; border-radius: 50%;
    border: 2px solid var(--brand-grey);
  }

  .card--back .brand-name {
    position: absolute; left: 0; right: 0; top: 118px;
    justify-content: center; font-size: 36px;
  }
  .card--back .brand-name__dot { width: 32px; height: 32px; }
  .card--back .website {
    position: absolute; left: 0; right: 0; bottom: 42px;
    text-align: center; font-size: 14px; color: var(--ink); letter-spacing: .5px;
  }

  .frame { position: absolute; inset: 0; }
  .frame__icons { position: absolute; left: 11px; top: 180px; display: flex; flex-direction: column; gap: 18px; }
  .frame__icons span { width: 8px; height: 8px; border-radius: 50%; background: var(--accent-dot); }

  .card--front .brand-name {
    position: absolute; right: 40px; top: 62px; font-size: 28px;
  }
  .card--front .brand-name__dot { width: 26px; height: 26px; }

  .contact { position: absolute; left: 52px; top: 130px; color: var(--ink); }
  .contact__name { font-size: 19px; font-weight: 500; line-height: 1.2; }
  .contact__title { font-size: 12px; color: var(--muted); margin-top: 2px; }
  .contact__address { font-size: 10px; color: var(--muted); margin-top: 10px; line-height: 1.5; }
  .contact__lines { font-size: 10px; color: var(--muted); margin-top: 10px; line-height: 1.7; }
</style>
</head>
<body>
<main class="stage">

  <section class="card card--back" aria-label="Card back">
    <div class="brand-name">
      <span class="brand-name__dot"></span>
      <span>Velvet &amp; Lark</span>
    </div>
    <p class="website">www.velvetlark-example.az</p>
  </section>

  <section class="card card--front" aria-label="Card front">
    <svg class="frame" viewBox="0 0 540 310" width="540" height="310" aria-hidden="true">
      <path d="M0 150 L30 150 L30 270 Q30 292 52 292 L540 292 L540 310 L0 310 Z" fill="var(--ink)"/>
    </svg>
    <div class="frame__icons" aria-hidden="true"><span></span><span></span><span></span><span></span></div>

    <div class="brand-name">
      <span class="brand-name__dot"></span>
      <span>Velvet &amp; Lark</span>
    </div>

    <div class="contact">
      <p class="contact__name">Nargiza Huseynova</p>
      <p class="contact__title">General Manager</p>
      <p class="contact__address">17 Samad Str. AZ 1014,<br>Baku, Azerbaijan</p>
      <p class="contact__lines">
        Tel: 012 555 0147<br>
        nargiza.huseynova@velvetlark-example.az<br>
        www.velvetlark-example.az
      </p>
    </div>
  </section>

</main>
</body>
</html>
```